Dr. Marissa Tevlin Medical/Chiropractic Business Card

Dr. Tevlin is a chiropractor and will require a business card that she uses every single day to book appointments on the back side of the card. Currently the office name goes by Dr. Marissa Tevlin. The chiropractic profession is based on the diagnosis and manipulative treatment of misalignments of the joints, especially those of the spinal column, which are held to cause other disorders by affecting the nerves, muscles, and organs. Dr. Marissa Tevlin is looking for a contemporary and minimalistic design.

Industry/Entity Type

Medical

Contact Information for Business Card

Name: Dr. Marissa Tevlin; Address: 748 Harcastle Rd South, London, ON N5R 2K7; Phone Number: 519.274.6193; Fax: 519.281.5046; email: marissa.tevlin@quorvamail.com

Requirements
Must have
• ability to write multiple appointments date/time on the back of card

```html
<!DOCTYPE html>
<html lang="en">
<head>
<meta charset="utf-8">
<title>Dr. Marissa Tevlin – Business Card</title>
<link rel="stylesheet" href="https://fonts.googleapis.com/css2?family=Roboto+Condensed:wght@700&family=Arimo:wght@400;700&family=Playfair+Display:ital,wght@1,800&display=swap">
<style>
  :root {
    --stage: #2f2f2f;
    --card: #ffffff;
    --brand-blue: #0f4f86;
    --brand-blue-dark: #0b416f;
    --band-grey: #4d4d4f;
    --text-grey: #6f6f71;
    --icon-grey: #707072;
    --ink: #111111;
    --spine-tone: #c3c9dc;
  }
  * { box-sizing: border-box; margin: 0; padding: 0; }
  html, body {
    width: 999px; height: 1200px; overflow: hidden;
    background: var(--stage);
  }
  .canvas { position: relative; width: 999px; height: 1200px; }

  .card {
    position: absolute; left: 37px; width: 925px;
    background: var(--card); overflow: hidden;
  }
  .card--front { top: 56px; height: 528px; }
  .card--back  { top: 611px; height: 529px; }

  /* Front */
  .identity { position: absolute; left: 66px; top: 186px; color: var(--brand-blue);
    font-family: "Roboto Condensed", "Arial Narrow", sans-serif; font-weight: 700; line-height: 1; }
  .identity__title { font-size: 34px; }
  .identity__name  { font-size: 62px; margin-top: 8px; letter-spacing: -0.5px; }
  .identity__role  { font-size: 34px; margin-top: 12px; letter-spacing: 0.5px; }

  .contact { position: absolute; left: 544px; top: 154px;
    font-family: "Arimo", Arial, sans-serif; color: var(--text-grey); }
  .contact__row { display: flex; align-items: center; position: relative; }
  .contact__icon { position: absolute; left: 0; fill: var(--icon-grey); }
  .contact__text { margin-left: 41px; font-size: 24px; line-height: 31px; }
  .contact__row--address { height: 62px; }
  .contact__row--address .contact__icon { top: 14px; }
  .contact__row--phone { margin-top: 18px; height: 44px; }
  .contact__row--phone .contact__text { font-size: 38px; font-weight: 700; }
  .contact__row--fax { margin-top: 0; height: 40px; }
  .contact__row--email { height: 40px; }
  .contact__row--email .contact__text { font-size: 23px; }

  .front-band { position: absolute; left: 0; top: 444px; }

  /* Back */
  .appt-header { position: absolute; left: 0; top: 0; width: 925px; height: 136px;
    background: linear-gradient(90deg, var(--brand-blue-dark), var(--brand-blue) 50%, var(--brand-blue-dark));
    display: flex; align-items: center; justify-content: center; }
  .appt-header__title { font-family: "Playfair Display", Georgia, serif; font-style: italic;
    font-weight: 800; font-size: 66px; color: #fff; letter-spacing: 1px; margin-top: 6px; }

  .spine-art { position: absolute; left: 435px; top: 142px; width: 80px; height: 296px;
    background: linear-gradient(180deg, rgba(195,201,220,0.4), var(--spine-tone) 50%, rgba(195,201,220,0.4));
    border-radius: 40px; }

  .appt-label { position: absolute; top: 172px; font-family: "Arimo", Arial, sans-serif;
    font-weight: 700; font-size: 28px; color: var(--ink); transform: translateX(-50%); }
  .appt-label--date { left: 260px; }
  .appt-label--time { left: 675px; }

  .appt-line { position: absolute; height: 3px; background: var(--ink); width: 360px; }
  .appt-line--date { left: 74px; }
  .appt-line--time { left: 490px; }

  .appt-note { position: absolute; left: 0; width: 925px; top: 442px; text-align: center;
    font-family: "Arimo", Arial, sans-serif; font-weight: 700; font-size: 23px;
    line-height: 31px; color: var(--ink); }
</style>
</head>
<body>
<main class="canvas">

  <section class="card card--front">
    <div class="identity">
      <div class="identity__title">DR.</div>
      <div class="identity__name">MARISSA TEVLIN</div>
      <div class="identity__role">CHIROPRACTOR</div>
    </div>

    <div class="contact">
      <div class="contact__row contact__row--address">
        <svg class="contact__icon" width="22" height="34" viewBox="0 0 22 34" aria-hidden="true">
          <path d="M11 0C4.9 0 0 4.9 0 11c0 7.5 11 23 11 23s11-15.5 11-23C22 4.9 17.1 0 11 0zm0 15.5a4.5 4.5 0 1 1 0-9 4.5 4.5 0 0 1 0 9z"/>
        </svg>
        <div class="contact__text">748 Harcastle Rd South<br>London, ON N5R 2K7</div>
      </div>
      <div class="contact__row contact__row--phone">
        <svg class="contact__icon" width="26" height="26" viewBox="0 0 24 24" aria-hidden="true">
          <path d="M6.6 10.8a15.1 15.1 0 0 0 6.6 6.6l2.2-2.2c.3-.3.7-.4 1-.2 1.1.4 2.3.6 3.6.6.6 0 1 .4 1 1V20c0 .6-.4 1-1 1C10.6 21 3 13.4 3 4c0-.6.4-1 1-1h3.5c.6 0 1 .4 1 1 0 1.3.2 2.5.6 3.6.1.3 0 .7-.2 1z"/>
        </svg>
        <div class="contact__text">519.274.6193</div>
      </div>
      <div class="contact__row contact__row--fax">
        <svg class="contact__icon" width="22" height="24" viewBox="0 0 22 24" aria-hidden="true">
          <rect x="5" y="0" width="12" height="9"/><rect x="0" y="10" width="22" height="10" rx="1"/><rect x="3" y="21" width="16" height="3"/>
        </svg>
        <div class="contact__text">519.281.5046</div>
      </div>
      <div class="contact__row contact__row--email">
        <svg class="contact__icon" width="24" height="22" viewBox="0 0 24 22" aria-hidden="true">
          <path d="M12 0 0 8v14h24V8zm0 14L3 8.5 12 3l9 5.5z"/>
        </svg>
        <div class="contact__text">marissa.tevlin@quorvamail.com</div>
      </div>
    </div>

    <svg class="front-band" width="925" height="84" viewBox="0 0 925 84" aria-hidden="true">
      <rect x="0" y="24" width="520" height="23" fill="var(--band-grey)"/>
      <path d="M0 47H470c25 0 35-10 50-25C535 7 550 0 570 0H925V84H0z" fill="var(--brand-blue)"/>
    </svg>
  </section>

  <section class="card card--back">
    <header class="appt-header"><h1 class="appt-header__title">APPOINTMENTS</h1></header>
    <div class="spine-art" role="img" aria-label="Faint spinal column illustration"></div>

    <div class="appt-label appt-label--date">Date</div>
    <div class="appt-label appt-label--time">Time</div>

    <div class="appt-line appt-line--date" style="top:238px"></div>
    <div class="appt-line appt-line--date" style="top:290px"></div>
    <div class="appt-line appt-line--date" style="top:341px"></div>
    <div class="appt-line appt-line--date" style="top:393px"></div>
    <div class="appt-line appt-line--time" style="top:238px"></div>
    <div class="appt-line appt-line--time" style="top:290px"></div>
    <div class="appt-line appt-line--time" style="top:341px"></div>
    <div class="appt-line appt-line--time" style="top:393px"></div>

    <p class="appt-note">If you are unable to make your appointment,<br>Please call us to reschedule</p>
  </section>

</main>
</body>
</html>
```